Webdesign für Industrieanlagenbau-Unternehmen
Zielgruppe
Die ZEV services GmbH ist ein ein österreichisches, eigentümergeführtes Industrieanlagenbau-Unternehmen mit Niederlassungen an derzeit 2 Standorten (Wendelsfeld/NÖ und Hallein/Sbg) und ist in den Geschäftsfeldern Industrieanlagenbau, Reinraumtechnik und Sondermaschinenbau - sowie im Projekt- und Behördenmanagement tätig.
Die ZEV services GmbH unterstützt ihre B2B-Kunden bei der Umsetzung von Engineering-Projekten in der Hightech-, Elektronik- und Prozessindustrie.
Unsere Kernkompetenzen sind Konzepterstellung, 3D-Planung, Konstruktion, Design und Montage von Prozessanlagen und Reinräumen, eine eigene Fertigung und Prototypenbau in unserer „Metall-& Kunststoff Manufaktur“ sowie die Abwicklung des Behörden-Managements wie z.B. Einreichverfahren nach Gewerbeordnung.
Langjährige und dauerhafte Geschäftsbeziehungen zu unseren Kunden stehen bei uns im Vordergrund.
Zielsgruppe der neuen website:
„Visitenkarte“ der ZEV services GmbH
potentielle Mitarbeiter („Employer Branding“), Ingenieure/Projektmanager (WI-Maschinenbau, Elektro- und Prozesstechnik), Mechatroniker, Schlosser, Elektriker
B2B Kunden aus Bereichen Mikroelektronik-Fertigung, chemische Industrie, Lebensmittel- und Pharmaproduktion
Bestandskunden (Stakeholder des „Buying Centers“ bei Kunden)
Neukunden „eingeschränkt“ (dzt. Keine aktive Kundenakquise via web geplant)
Aufgabenstellung
Allgemeine Anforderungen an die neue website:
Ziel sind eher „schlanke“ Texte & Design (vgl. https://www.valdrin-gruppe.com/de/)
Produkt- und Leistungsspezifisches Bildmaterial sollen hauptsächlich ZEV-eigene Fotos und Videos sein (Stock-Fotos nur für Allgemeine Bilder). Beispielhaftes Bildmaterial (sollte durch ZEV Mitarbeiter dann im CMS einfach ausgetauscht werden können) in diesen Unterlagen
CMS (Content Management System) zur Administration durch ZEV Mitarbeiter
Hosting auf europäischen ServernServern (z.B. https://voll-pack.com/, https://www.brommlat.com, https://www.kessfurt.de, https://www.ornix2go.com/, https://www.puvo.at)
Basierend auf weitverbreiteten open-Source Systemen (z.B. Wordpress , Joomla, TYPO3)
Responsive Webdesign – eine Website für alle Geräte (PC, Tablet, Smartphone) und alle gängigen Browser (Chrome, Edge, Safari, Firefox, Opera, Internet Explorer)
Google Pagespeed mind. 85 Punkte, GTmetrix Grade > 80%
Sicherheitszertifikat (SSL-Zertifikat)
Sprache – Deutsch, Englisch
E-Commerce-Gesetz (ECG) & DSGVO konform (Cookie Disclaimer Standard „nur notwendige“)
Impressum
AGB - Allgemeine Lieferungs- und Zahlungsbedingungen
Sitemap
Vollständige Rechte an der website (Design, Inhalt etc.) bei ZEV services GmbH
Einbettung von Text, Fotos und Videos durch ZEV Mitarbeiter
Hinzufügen von Menü-Unterpunkten durch ZEV Mitarbeiter

```html
<!DOCTYPE html>
<html lang="de">
<head>
<meta charset="utf-8">
<title>ZEV services GmbH – Leistungen</title>
<link href="https://fonts.googleapis.com/css2?family=Barlow:wght@400;500;600&family=Josefin+Slab:wght@400;600&display=swap" rel="stylesheet">
<style>
:root{
  --accent:#e2463b;
  --label:#e8695a;
  --ink:#3a3a3a;
  --ink-soft:#555;
  --grey:#e9eaec;
  --grey-dark:#d6d8db;
  --white:#fff;
}
*{box-sizing:border-box;margin:0;padding:0}
html,body{width:1200px;height:4272px;overflow:hidden;background:var(--white)}
body{position:relative;font-family:"Barlow",sans-serif;color:var(--ink);font-size:12px;line-height:16px}
.abs{position:absolute}
.brand{left:33px;top:18px;display:flex;align-items:center;gap:7px;color:var(--accent);font-weight:600;font-size:24px;line-height:24px}
.brand i{width:18px;height:18px;background:var(--accent);display:block}
.nav{left:465px;top:22px;display:flex;gap:26px;font-family:"Josefin Slab",serif;font-size:12px;font-weight:600}
.nav .active{color:var(--accent)}
.nav-right{left:1034px;top:22px;display:flex;gap:24px;font-family:"Josefin Slab",serif;font-size:12px;font-weight:600}
.hero{left:31px;top:63px;width:1137px;height:542px;background:linear-gradient(160deg,#2c3a52 0%,#8b98ad 45%,#c9d1dc 70%,#3d4960 100%)}
.hero-box{left:36px;top:457px;width:564px;height:143px;background:var(--grey)}
.hero-box h1{position:absolute;left:32px;top:30px;font-family:"Josefin Slab",serif;font-weight:400;font-size:33px;letter-spacing:4px;line-height:40px}
.hero-box .down{position:absolute;left:32px;top:78px;width:32px;height:32px;border:1px solid var(--ink);display:flex;align-items:center;justify-content:center}
.h2{font-family:"Josefin Slab",serif;font-weight:400;font-size:31px;letter-spacing:3px;line-height:35px}
.right{text-align:right}
.label{color:var(--label);font-size:13px}
.text{font-size:12px;line-height:16px;color:var(--ink-soft)}
.list{list-style:none;margin-top:10px}
.list li{position:relative;padding-left:15px;line-height:19px}
.list li::before{content:"";position:absolute;left:0;top:6px;width:8px;height:8px;border-radius:50%;background:#888}
.frame{background:var(--grey)}
.photo{position:absolute}
.dots{position:absolute;display:flex;gap:5px}
.dots span{width:4px;height:4px;background:#555}
.dots span:first-child{width:6px;height:6px;margin-top:-1px}
.band{left:0;top:2570px;width:1200px;height:955px;background:var(--grey)}
.prod-h{font-family:"Josefin Slab",serif;font-weight:600;font-size:14px;border-bottom:1px solid var(--ink);padding-bottom:3px}
.cta{left:31px;top:3468px;font-family:"Josefin Slab",serif;font-weight:600;font-size:13px;letter-spacing:1px;border-bottom:1px solid var(--ink);padding-bottom:6px}
.foot-brand{left:249px;top:4152px;display:flex;align-items:center;gap:6px;font-weight:600;font-size:17px}
.foot-brand i{width:13px;height:13px;background:var(--ink);display:block}
.foot-addr{left:322px;top:4148px;font-size:8px;line-height:12px;color:var(--ink)}
.badge{position:absolute;top:4150px;width:30px;height:30px}
.copy{left:873px;top:4158px;font-size:8px;color:var(--ink-soft)}
.to-top{left:1157px;top:4172px;width:33px;height:33px;background:var(--grey);display:flex;align-items:center;justify-content:center}
</style>
</head>
<body>

<div class="abs brand"><i></i>ZEV</div>
<nav class="abs nav"><span>Home</span><span class="active">Leistungen</span><span>Kontakt</span><span>Jobs/Karriere</span></nav>
<div class="abs nav-right"><span>Kunden-Portal</span><span>DE</span></div>

<div class="abs hero" role="img" aria-label="Foto: Rohrleitungen und Lüftungskanäle einer Industrieanlage"></div>
<div class="abs hero-box">
  <h1>UNSERE LEISTUNGEN</h1>
  <div class="down"><svg width="10" height="6" viewBox="0 0 10 6"><path d="M1 1l4 4 4-4" fill="none" stroke="#3a3a3a" stroke-width="1.3"/></svg></div>
</div>

<h2 class="abs h2" style="left:250px;top:685px">Muster Einführungstext</h2>
<p class="abs text" style="left:255px;top:758px;width:690px">Muster Text Lorem ipsum dolor sit amet, consetetur sadipscing elitr, sed diam nonumy eirmod tempor invidunt ut labore et dolore magna aliquyam erat, sed diam voluptua. At vero eos et accusam et justo duo dolores et ea rebum. Stet clita kasd gubergren, no sea takimata sanctus est Lorem ipsum dolor sit amet. Lorem ipsum dolor sit amet, consetetur sadipscing elitr, sed diam nonumy eirmod tempor invidunt ut labore et dolore magna aliquyam erat, sed diam voluptua. At vero eos et accusam et justo duo dolores et ea rebum. Stet clita kasd gubergren, no sea takimata sanctus est Lorem ipsum dolor sit amet. Lorem ipsum dolor sit amet, consetetur sadipscing elitr, sed diam nonumy eirmod tempor invidunt ut labore et dolore magna aliquyam erat, sed diam voluptua. At vero eos et accusam et justo duo dolores et ea rebum. Stet clita kasd gubergren.</p>

<div class="abs label right" style="left:600px;top:975px;width:345px">Industrieanlagenbau</div>
<h2 class="abs h2 right" style="left:250px;top:1002px;width:698px">Nach Kundenwunsch und entsprechend<br>der Anforderungen konstruiert und<br>gefertigt</h2>
<div class="abs text" style="left:255px;top:1160px;width:400px">
  <p>In enger Zusammenarbeit mit Ihnen übernimmt ZEV services GmbH als Komplettanbieter den Neubau oder Modernisierung Ihrer Prozessanlagen.</p>
  <p style="margin-top:12px">Unser Portfolio:</p>
  <ul class="list">
    <li>Konzepterstellung &amp; Design</li>
    <li>Engineering &amp; 3D-Detailplanung</li>
    <li>Automatisierung</li>
    <li>Montage &amp; Inbetriebnahme</li>
    <li>CE-Kennzeichnung</li>
    <li>Behörden-Management und Einreichverfahren</li>
  </ul>
</div>
<div class="abs frame" style="left:711px;top:1142px;width:234px;height:232px">
  <div class="photo" role="img" aria-label="Foto: Fertigungshalle mit Prozessanlagen" style="left:7px;top:63px;width:220px;height:106px;background:linear-gradient(180deg,#9aa3ab,#6c6257)"></div>
  <div class="dots" style="left:97px;top:222px"><span></span><span></span><span></span><span></span></div>
</div>

<div class="abs label" style="left:250px;top:1468px">Reinraumtechnik</div>
<h2 class="abs h2" style="left:250px;top:1497px">Ihr erfahrenes Unternehmen für<br>anspruchsvolle Reinraum-Lösungen</h2>
<div class="abs frame" style="left:255px;top:1602px;width:408px;height:151px">
  <div class="photo" role="img" aria-label="3D-Planung eines Reinraum-Gebäudes" style="left:9px;top:10px;width:390px;height:126px;background:linear-gradient(180deg,#cfd2d4,#7e868a)"></div>
  <div class="dots" style="left:195px;top:142px"><span></span><span></span></div>
</div>
<p class="abs text" style="left:676px;top:1624px;width:270px">Neben der Auslegung der Systeme zur Luftaufbereitung und -förderung planen wir gemeinsam mit Ihnen alle Funktionselemente und Komponenten wie Reinraumwände, -decken und -böden.<br>Unsere Leistung umfasst Konzepterstellung, Prozess- und Detailplanung.</p>

<div class="abs label right" style="left:600px;top:1848px;width:345px">Sondermaschinenbau</div>
<h2 class="abs h2 right" style="left:250px;top:1875px;width:698px">Von der einfachen Zuführung bis hin zur<br>komplexen Montageanlage</h2>
<div class="abs text" style="left:255px;top:1984px;width:405px">
  <p>Neben kundenindividuellen Lösungen und Assemblierung von Komponenten konstruieren wir unter anderem Abfüll- und Mischanlagen für verschiedene Industriezweige.<br>Für den Rohrleitungsbau von Primär- &amp; Sekundärkühlkreislauf haben wir die Konstruktion &amp; 3D- Planung im Haus.</p>
  <p style="margin-top:16px">Wir planen, fertigen und montieren die Infrastruktur für Rack-Lösungen (Gerätebühnen, Zwischenböden, Podeste, usw.) und Löschsysteme für IT-Räume/Racks (gasförmige Löschmittel).</p>
</div>
<div class="abs frame" style="left:711px;top:1982px;width:234px;height:149px">
  <div class="photo" role="img" aria-label="Foto: Montageanlage in einer Halle" style="left:65px;top:4px;width:104px;height:141px;background:linear-gradient(180deg,#b8a98a,#3f4246)"></div>
</div>

<div class="abs label" style="left:250px;top:2226px">Gasversorgungsanlagen</div>
<h2 class="abs h2" style="left:250px;top:2253px">Gasversorgungsanlagen für höchste<br>Ansprüche</h2>
<div class="abs frame" style="left:255px;top:2358px;width:477px;height:124px">
  <div class="photo" role="img" aria-label="Foto: Gasversorgungsanlage mit Armaturen" style="left:164px;top:7px;width:151px;height:111px;background:linear-gradient(180deg,#e4e4e4,#8d8f92)"></div>
</div>
<p class="abs text" style="left:746px;top:2373px;width:200px">Planung und Konstruktion von industriellen Abfüllanlagen für Versandbehälter, Zentralen Gasversorgungsanlagen (ZGVs) inklusive Analytik und Gaswarnanlagen.</p>

<div class="abs band"></div>
<div class="abs label" style="left:0;top:2603px;width:1195px;text-align:center">Produkte</div>
<h2 class="abs h2" style="left:0;top:2630px;width:1195px;text-align:center">Produkte von ZEV Services</h2>

<div class="abs prod-h" style="left:262px;top:2707px;width:676px">Materialschleusen für Reinräume</div>
<div class="abs text" style="left:262px;top:2743px;width:676px">
  <p>Eine Reinraumschleuse dient zum Transport von Teilen zwischen zwei Räumlichkeiten unterschiedlicher Reinraumklassen, ohne das eine wechselseitige Kontamination auftreten kann.</p>
  <p style="margin-top:12px">ZEV services GmbH passt die Reinraumschleuse kundenindividuell an:</p>
  <ul class="list">
    <li>Größe/Abmessungen entsprechend Ihren Anforderungen</li>
    <li>Anbindung an Ihr Prozessleitsystem</li>
    <li>Anbindung an Ihr Prozessleitsystem</li>
    <li>Option: Dekontaminationsprozess mit H2O2 - Wasserstoffperoxid (für pharmazeutische Industrie und Krankenhäuser)</li>
  </ul>
</div>
<div class="abs photo" role="img" aria-label="Produktfoto: Materialschleuse freistehend" style="left:262px;top:2900px;width:136px;height:154px;background:linear-gradient(180deg,#f4f4f4,#b9bcbf)"></div>
<div class="abs photo" role="img" aria-label="Produktfoto: Materialschleuse eingebaut" style="left:416px;top:2900px;width:96px;height:154px;background:linear-gradient(180deg,#d9d7d2,#8a857c)"></div>

<div class="abs prod-h" style="left:262px;top:3105px;width:212px">Heizungs- &amp; Kälteverteiler</div>
<p class="abs text" style="left:262px;top:3141px;width:212px">Flexibel konfigurierte hydraulische Verteilersysteme zum Abführen hoher Wärmelasten z.B. aus Serverschränken oder für individuelle Kühlungs- bzw. Wärmeanforderungen.</p>
<div class="abs photo" role="img" aria-label="3D-Darstellung eines hydraulischen Verteilers" style="left:262px;top:3234px;width:212px;height:138px;background:linear-gradient(180deg,#e5e6e7,#7b7f82)"></div>

<div class="abs prod-h" style="left:512px;top:3105px;width:426px">Heizungs- &amp; Kälteverteiler</div>
<p class="abs text" style="left:512px;top:3141px;width:426px">Durch ein Wärmetauscher-System wird der Sekundärkreislauf (zu den zu kühlenden bzw. zu wärmenden Anlagen) vom Primärkreislauf (Hauptkühl- bzw. -wärmekreislauf) getrennt. Die kompakte Bauweise und hocheffiziente Komponenten der ZEV Wärmetauscher-Station garantiert dauerhaft stabile Durchfluss- und Temperaturprofile im Primärkreislauf der zu kühlenden bzw. wärmenden Anlagen.Die kundenspezifische Fertigung erfolgt an unserem Standort in Wendelsfeld/NÖ.</p>
<div class="abs photo" role="img" aria-label="Produktfoto: Wärmetauscher-Station" style="left:512px;top:3264px;width:91px;height:154px;background:linear-gradient(180deg,#eeeeee,#8e9194)"></div>
<div class="abs photo" role="img" aria-label="Produktfoto: Wärmetauscher-Station mit Rohrleitungen" style="left:611px;top:3264px;width:92px;height:154px;background:linear-gradient(180deg,#cfcfcf,#2d2f33)"></div>

<div class="abs cta">KONTAKT AUFNEHMEN <svg width="7" height="9" viewBox="0 0 7 9" style="margin-left:4px"><path d="M1 1l4 3.5L1 8" fill="none" stroke="#3a3a3a" stroke-width="1.2"/></svg></div>

<div class="abs label" style="left:606px;top:3608px">Projekt-Management und Behörden-Management</div>
<h2 class="abs h2" style="left:606px;top:3635px">Ein erfahrenes<br>Engineering Team</h2>
<div class="abs frame" style="left:250px;top:3775px;width:343px;height:93px"></div>
<div class="abs frame" style="left:250px;top:3947px;width:699px;height:96px"></div>
<div class="abs photo" role="img" aria-label="Foto: Firmengebäude der ZEV services GmbH" style="left:257px;top:3874px;width:330px;height:133px;background:linear-gradient(180deg,#9ea4ab,#3e4348)"></div>
<div class="abs text" style="left:606px;top:3735px;width:340px">
  <p>Mit unserem erfahrenen Engineering Team unterstützen wir Sie beim effizienten, sinnvollen und wirtschaftlichen Umgang mit Ihren Ressourcen.<br>Unsere Leistungen umfassen unter anderem:</p>
  <ul class="list" style="margin-top:16px">
    <li>Behördenmanagement (Gewerbebehördliche Genehmigung)</li>
    <li>Konformitätsbewertung (CE)</li>
    <li>Baustellenkoordination</li>
    <li>Explosionsschutz</li>
    <li>Dokumentation Arbeitnehmerschutz</li>
    <li>Technische Dokumentation</li>
    <li>Training / Unterweisung</li>
    <li>Inbetriebnahme &amp; Übergabe</li>
  </ul>
</div>

<div class="abs foot-brand"><i></i>ZEV</div>
<div class="abs foot-addr"><b>ZEV services GmbH</b> - Werkstraße 12, A-9990<br>Wendelsfeld / <u>www.zev-services.at</u> /<br><u>office@zev-services.at</u> / <u>+43 5555 000 000</u></div>
<svg class="badge" style="left:545px" viewBox="0 0 30 30"><circle cx="15" cy="15" r="14" fill="#4a78b8"/></svg>
<svg class="badge" style="left:598px" viewBox="0 0 30 30"><rect x="2" y="2" width="26" height="26" fill="#e07a6a"/></svg>
<svg class="badge" style="left:670px" viewBox="0 0 30 30"><rect x="2" y="2" width="26" height="26" fill="#2f8a7a"/></svg>
<svg class="badge" style="left:705px" viewBox="0 0 30 30"><circle cx="15" cy="15" r="14" fill="#2d4f95"/></svg>
<div class="abs copy">© ZEV services GmbH</div>
<div class="abs to-top"><svg width="10" height="6" viewBox="0 0 10 6"><path d="M1 5l4-4 4 4" fill="none" stroke="#777" stroke-width="1.2"/></svg></div>

</body>
</html>
```